KD Summit Fitness personal training needs a new Business Card design for 2016

Business Card design:
Our current business card is very plain
We are bringing on our first team member next year and thought its a perfect time to have a new face lift for our company!

We are a Personal Training business "KD Summit Fitness" who specializes in strength and conditioning / weightloss training,
We also run a yearly Bootcamp called "Ferocity Bootcamps", this is our Logo Design which we are looking for

The pink and blue in the logo are our business colours, how ever we don't want those colours to heavily dominate the card.

We are looking for a business card which is eye catching, and creative.

I am open to suggestions and any designs :)

Logo Design:

For our Logo Design we are looking for a bright, energetic logo, preferably a word logo which portrays strength and high intensity
If it has icon's etc in it thats fine again im open for suggestions :)
The Logo Design is for our Bootcamp which runs yearly
The bootcamp is called "Ferocity Bootcamp"

Target Market(s)

Age 20-40
Individuals who want to look great and have more energy

Industry/Entity Type

Business

Contact Information for Business Card

On the front
KD Summit Fitness Derwin Okoye Personal Training / Bootcamps / Pilates / Nutrition Healthy mind, Healthy body, Ultimate lifestyle < our slogan
Icons for the following
Email:
Mobile:
Facebook:
Instagram:

On the back we would like to include somewhere
"Show this card to receive 50% off your first 30min pt session"
"Valid to one user only"

Logo Text

Ferocity Bootcamp

Font styles to use
Serif

Colors
e34197
0255a3
000000
ffffff

Requirements
Must have
• - Icons for instagram, facebook, email and mobile phone
• - Slogan: Healthy mind, Healthy body, Ultimate lifestyle
• - What we offer: Personal Training , Bootcamps, Pilates, Nutrition
• - Logo
• -
Nice to have
• - Our 50% offer on the back
• - a place for a photo
Should not have
• - Pink and Blue everywhere

```html
<!DOCTYPE html>
<html lang="en">
<head>
<meta charset="utf-8">
<title>KD Summit Fitness – Business Card</title>
<link href="https://fonts.googleapis.com/css2?family=Anton&family=Oswald:wght@400;600&family=Lobster&display=swap" rel="stylesheet">
<style>
  :root{
    --pink:#e34197;
    --pink-soft:#f28ac3;
    --pink-deep:#c8347f;
    --blue:#0255a3;
    --blue-mid:#3a6fd8;
    --blue-light:#6a95ea;
    --blue-dark:#2f5fc9;
    --white:#ffffff;
    --ink:#000000;
    --stage:#ececef;
  }
  *{box-sizing:border-box;margin:0;padding:0}
  html,body{width:1200px;height:1000px;overflow:hidden;background:var(--stage)}
  .canvas{position:relative;width:1200px;height:1000px}
  .card{position:absolute;left:215px;width:770px;height:440px;overflow:hidden;box-shadow:0 10px 30px rgba(0,0,0,.18)}

  /* ---------- back ---------- */
  .card-back{top:40px;background:linear-gradient(135deg,var(--blue-light) 0%,var(--blue-mid) 55%,var(--blue-dark) 100%);color:var(--white);text-align:center}
  .back-texture{position:absolute;inset:0;background:radial-gradient(ellipse at 75% 20%,rgba(255,255,255,.25),transparent 55%),radial-gradient(ellipse at 10% 90%,rgba(255,255,255,.18),transparent 50%)}
  .brand{display:inline-flex;align-items:center;gap:10px;font-family:"Oswald",sans-serif;font-weight:600;font-size:22px;letter-spacing:2px;text-transform:uppercase;color:var(--white);white-space:nowrap}
  .brand-dot{width:30px;height:30px;border-radius:50%;background:var(--white)}
  .back-content{position:relative;padding-top:46px}
  .offer-lead{font-family:"Anton",sans-serif;font-size:42px;letter-spacing:1px;margin-top:26px;text-transform:uppercase}
  .offer-amount{font-family:"Anton",sans-serif;font-size:128px;line-height:1;color:var(--pink);margin-top:2px;text-transform:uppercase}
  .offer-detail{font-family:"Anton",sans-serif;font-size:38px;letter-spacing:1px;text-transform:uppercase;margin-top:6px}
  .offer-terms{font-family:"Oswald",sans-serif;font-size:20px;letter-spacing:2px;font-style:italic;text-transform:uppercase;margin-top:10px}

  /* ---------- front ---------- */
  .card-front{top:520px;background:var(--white)}
  .edge-pink{position:absolute;left:0;top:0;width:12px;height:100%;background:var(--pink)}
  .front-brand{position:absolute;left:300px;top:20px}
  .front-brand .brand{color:var(--blue);font-size:20px}
  .front-brand .brand-dot{background:var(--blue)}
  .contact-strip{position:absolute;left:12px;right:0;top:74px;height:38px;display:flex}
  .contact{display:flex;align-items:center;gap:8px;padding:0 14px;font-family:"Oswald",sans-serif;font-size:15px;color:var(--white);letter-spacing:.5px;white-space:nowrap}
  .contact svg{flex:none}
  .contact.phone{background:var(--blue);width:372px;justify-content:flex-end}
  .contact.facebook{background:var(--pink);flex:1}
  .contact.instagram{background:var(--blue);flex:1}
  .photo{position:absolute;left:384px;top:112px;right:34px;bottom:0;background:linear-gradient(160deg,var(--pink-soft) 0%,var(--pink) 60%,var(--pink-deep) 100%)}
  .photo-stripes{position:absolute;right:0;top:112px;bottom:0;width:34px;background:repeating-linear-gradient(90deg,var(--blue) 0 6px,var(--white) 6px 10px)}
  .identity{position:absolute;left:36px;top:176px;width:336px}
  .name{font-family:"Anton",sans-serif;font-size:50px;line-height:1;text-transform:uppercase;white-space:nowrap}
  .name .first{color:var(--pink)}
  .name .last{color:var(--blue)}
  .services{margin-top:10px;font-family:"Oswald",sans-serif;font-weight:600;font-size:11.5px;color:var(--blue);text-transform:uppercase;letter-spacing:.2px;white-space:nowrap}
  .contact.email{position:absolute;left:12px;top:378px;width:372px;height:36px;background:var(--pink)}
  .wordmark{position:absolute;left:404px;top:176px;width:312px;color:var(--blue);text-align:center}
  .wordmark-main{font-family:"Anton",sans-serif;font-size:58px;line-height:1;text-transform:uppercase;white-space:nowrap}
  .wordmark-sub{font-family:"Oswald",sans-serif;font-weight:600;font-size:22px;letter-spacing:14px;text-transform:uppercase;margin-top:4px;padding-left:14px}
  .slogan{position:absolute;left:404px;top:336px;width:312px;text-align:center;font-family:"Lobster",cursive;font-size:24px;line-height:1.3;color:var(--white)}
</style>
</head>
<body>
<main class="canvas">

  <section class="card card-back" aria-label="Business card back">
    <div class="back-texture"></div>
    <div class="back-content">
      <div class="brand"><span class="brand-dot"></span>KD Summit Fitness</div>
      <p class="offer-lead">Show this card to receive</p>
      <p class="offer-amount">50% Off</p>
      <p class="offer-detail">Your first 30min PT session</p>
      <p class="offer-terms">"Valid to one user only"</p>
    </div>
  </section>

  <section class="card card-front" aria-label="Business card front">
    <div class="edge-pink"></div>
    <div class="front-brand"><div class="brand"><span class="brand-dot"></span>KD Summit Fitness</div></div>

    <div class="contact-strip">
      <div class="contact phone">
        <svg width="14" height="14" viewBox="0 0 24 24" aria-hidden="true"><path fill="#fff" d="M6.6 10.8a15.1 15.1 0 006.6 6.6l2.2-2.2a1 1 0 011-.25 11.4 11.4 0 003.6.57 1 1 0 011 1V20a1 1 0 01-1 1A17 17 0 013 4a1 1 0 011-1h3.5a1 1 0 011 1c0 1.25.2 2.45.57 3.57a1 1 0 01-.25 1z"/></svg>
        0400 318 762
      </div>
      <div class="contact facebook">
        <svg width="14" height="14" viewBox="0 0 16 16" aria-hidden="true"><circle cx="8" cy="8" r="7" fill="none" stroke="#fff" stroke-width="1.4"/><ellipse cx="8" cy="8" rx="3" ry="7" fill="none" stroke="#fff" stroke-width="1.2"/><path d="M1 8h14" stroke="#fff" stroke-width="1.2"/></svg>
        /kdsummitfitness
      </div>
      <div class="contact instagram">
        <svg width="14" height="14" viewBox="0 0 16 16" aria-hidden="true"><path d="M2 2.5h12v8.5H7l-3.5 3v-3H2z" fill="none" stroke="#fff" stroke-width="1.4" stroke-linejoin="round"/></svg>
        /derwinokoye_pt
      </div>
    </div>

    <div class="photo" role="img" aria-label="Pink-toned photo of a group training session"></div>
    <div class="photo-stripes"></div>

    <div class="identity">
      <h1 class="name"><span class="first">Derwin</span> <span class="last">Okoye</span></h1>
      <p class="services">Personal Training / Bootcamps / Pilates / Nutrition</p>
    </div>

    <div class="contact email">
      <svg width="16" height="12" viewBox="0 0 16 12" aria-hidden="true"><rect x="0.5" y="0.5" width="15" height="11" fill="none" stroke="#fff"/><path d="M0.5 0.5L8 7l7.5-6.5" fill="none" stroke="#fff"/></svg>
      hello@kdsummitfit.com
    </div>

    <div class="wordmark">
      <div class="wordmark-main">KD Summit</div>
      <div class="wordmark-sub">Fitness</div>
    </div>
    <p class="slogan">Healthy mind, Healthy body, Ultimate lifestyle</p>
  </section>

</main>
</body>
</html>
```